Coffee Shop needs a fresh new menu

Hi,
I would like a new menu to be designed for our coffee shop.
We display our menu on a television screen, so would need it in a file that would allow us to continue to do so -- I have attached a photo so that you can see our current design, and how it is displayed.

I'd like something that is easy to read, if the design could have a "hipster" feel to it -- we are located at a hospital and University.

I have attached a Word file with what we would like on the menu.

Feel free to contact me if you have any questions.

Thanks,
Liv

Just A4 size will be fine, and no need to include menu 1 and menu 2 - I just put them in as an example of what we already have -- they are our printed menu's. Thanks

Hospital

```html
<!DOCTYPE html>
<html lang="en">
<head>
<meta charset="utf-8">
<title>Ward Nine Canteen – Menu</title>
<link href="https://fonts.googleapis.com/css2?family=Arimo:wght@400;700&family=Cabin:wght@400;600;700&family=Sniglet:wght@800&display=swap" rel="stylesheet">
<style>
  :root {
    --board: #4a4545;
    --mint: #c6ebe8;
    --mint-deep: #9fd3cf;
    --pink: #f7d3e2;
    --pink-deep: #e7b3c9;
    --ink: #4a4545;
    --white: #ffffff;
  }
  * { margin: 0; padding: 0; box-sizing: border-box; }
  html, body { width: 1200px; height: 848px; overflow: hidden; background: var(--board); }
  .menu {
    position: relative; width: 1200px; height: 848px;
    background: var(--board); color: var(--white);
    font-family: "Cabin", sans-serif; overflow: hidden;
  }
  .deco { position: absolute; border-radius: 10px; opacity: .55; }
  .deco--mint { background: var(--mint); }
  .deco--pink { background: var(--pink); }
  .deco--soft { background: linear-gradient(180deg, var(--mint), rgba(198,235,232,.35)); opacity: .35; }

  .sign-lines { position: absolute; left: 0; top: 0; }
  .sign-name {
    position: absolute; left: 60px; top: 240px; width: 235px; text-align: center;
    font-family: "Cabin", sans-serif; font-weight: 700; font-size: 30px; color: var(--mint);
    line-height: 1.1;
  }

  .ribbon { position: absolute; }
  .ribbon svg { display: block; }
  .ribbon__label {
    position: absolute; left: 0; right: 0; top: 0; bottom: 0;
    display: flex; align-items: center; justify-content: center;
    font-family: "Sniglet", sans-serif; font-weight: 800; font-size: 18px; color: var(--ink);
    padding-bottom: 6px;
  }

  .coffee-table {
    position: absolute; left: 469px; top: 86px;
    font-family: "Arimo", sans-serif; font-size: 18px; line-height: 24px;
    border-collapse: collapse;
  }
  .coffee-table th { font-weight: 700; text-align: left; }
  .coffee-table td, .coffee-table th { padding: 0; }
  .coffee-table .drink { width: 150px; }
  .coffee-table .size-s { width: 68px; font-weight: 700; }
  .coffee-table .size-l { font-weight: 700; }
  .coffee-table th.size-s { padding-left: 15px; }
  .coffee-table th.size-l { padding-left: 22px; }

  .short-list {
    position: absolute; left: 455px; width: 300px; top: 312px; text-align: center;
    font-family: "Arimo", sans-serif; font-size: 18px; line-height: 24px;
  }
  .price { font-weight: 700; color: var(--mint); }
  .coffee-table .price, .short-list .price, .extras .price { color: var(--white); }

  .extras {
    position: absolute; left: 250px; width: 710px; top: 418px; text-align: center;
    font-family: "Arimo", sans-serif; font-size: 18px; line-height: 24px;
  }
  .extras__title { font-weight: 700; }

  .food-list {
    position: absolute; text-align: center; list-style: none;
    font-size: 17.5px; line-height: 24px;
  }
  .food-list--breakfast { left: 20px; width: 345px; top: 543px; }
  .food-list--light { left: 455px; width: 300px; top: 602px; }
  .food-list--hot { left: 840px; width: 340px; top: 540px; }
  .food-list .price { font-weight: 700; }
</style>
</head>
<body>
<main class="menu">

  <!-- hanging sign -->
  <svg class="sign-lines" width="380" height="390" viewBox="0 0 380 390" aria-hidden="true">
    <line x1="0" y1="18" x2="360" y2="18" stroke="var(--mint)" stroke-width="4" stroke-linecap="round"/>
    <line x1="95" y1="51" x2="260" y2="51" stroke="var(--pink)" stroke-width="2"/>
    <polyline points="252,45 262,51 252,57" fill="none" stroke="var(--pink)" stroke-width="2"/>
    <line x1="68" y1="22" x2="68" y2="170" stroke="var(--mint)" stroke-width="3" stroke-dasharray="8 4"/>
    <line x1="284" y1="22" x2="284" y2="170" stroke="var(--mint)" stroke-width="3" stroke-dasharray="8 4"/>
    <rect x="38" y="170" width="277" height="200" rx="40" fill="none" stroke="var(--mint)" stroke-width="2.5"/>
  </svg>
  <div class="sign-name">Ward Nine<br>Canteen</div>

  <!-- decorative illustrations -->
  <div class="deco deco--soft" role="img" aria-label="Hanging birdcage illustration" style="left:870px;top:0;width:140px;height:350px"></div>
  <div class="deco deco--soft" role="img" aria-label="Small bird illustration" style="left:330px;top:95px;width:85px;height:105px"></div>
  <div class="deco deco--soft" role="img" aria-label="Small bird illustration" style="left:785px;top:155px;width:80px;height:105px"></div>
  <div class="deco deco--soft" role="img" aria-label="Small bird illustration" style="left:1098px;top:95px;width:85px;height:105px"></div>
  <div class="deco deco--pink" role="img" aria-label="Pink bird illustration" style="left:365px;top:685px;width:80px;height:105px;opacity:.35"></div>
  <div class="deco deco--mint" role="img" aria-label="Mint bird illustration" style="left:770px;top:625px;width:80px;height:105px;opacity:.35"></div>
  <div class="deco deco--pink" role="img" aria-label="Heart ornament" style="left:155px;top:93px;width:40px;height:36px"></div>
  <div class="deco deco--pink" role="img" aria-label="Heart ornament" style="left:845px;top:30px;width:42px;height:38px"></div>
  <div class="deco deco--pink" role="img" aria-label="Heart ornament" style="left:372px;top:330px;width:48px;height:45px"></div>
  <div class="deco deco--pink" role="img" aria-label="Heart ornament" style="left:1050px;top:372px;width:40px;height:38px"></div>
  <div class="deco deco--pink" role="img" aria-label="Heart ornament" style="left:1140px;top:688px;width:42px;height:38px"></div>
  <div class="deco deco--pink" role="img" aria-label="Heart ornament" style="left:25px;top:763px;width:42px;height:38px"></div>
  <div class="deco deco--pink" role="img" aria-label="Key ornament" style="left:16px;top:375px;width:45px;height:45px;opacity:.3"></div>
  <div class="deco deco--pink" role="img" aria-label="Key ornament" style="left:778px;top:352px;width:50px;height:40px;opacity:.3"></div>
  <div class="deco deco--pink" role="img" aria-label="Key ornament" style="left:1125px;top:15px;width:55px;height:25px;opacity:.3"></div>
  <div class="deco deco--mint" role="img" aria-label="Flourish ornament" style="left:560px;top:472px;width:90px;height:18px;opacity:.3"></div>
  <div class="deco deco--mint" role="img" aria-label="Flourish ornament" style="left:135px;top:767px;width:105px;height:16px;opacity:.3"></div>
  <div class="deco deco--pink" role="img" aria-label="Flourish ornament" style="left:565px;top:800px;width:90px;height:20px;opacity:.3"></div>
  <div class="deco deco--mint" role="img" aria-label="Flourish ornament" style="left:975px;top:810px;width:105px;height:16px;opacity:.3"></div>

  <!-- ribbons -->
  <div class="ribbon" style="left:500px;top:5px">
    <svg width="240" height="70" viewBox="0 0 240 70" aria-hidden="true">
      <polygon points="0,26 44,26 44,62 0,62 14,44" fill="var(--mint-deep)"/>
      <polygon points="240,26 196,26 196,62 240,62 226,44" fill="var(--mint-deep)"/>
      <path d="M30,10 Q120,26 210,10 L210,48 Q120,64 30,48Z" fill="var(--mint)"/>
    </svg>
    <div class="ribbon__label">Coffee</div>
  </div>
  <div class="ribbon" style="left:35px;top:440px;transform:rotate(-2deg)">
    <svg width="310" height="85" viewBox="0 0 310 85" aria-hidden="true">
      <polygon points="0,34 56,34 56,78 0,78 18,56" fill="var(--mint-deep)"/>
      <polygon points="310,30 254,30 254,74 310,74 292,52" fill="var(--mint-deep)"/>
      <path d="M38,12 Q155,30 272,10 L272,60 Q155,80 38,62Z" fill="var(--mint)"/>
    </svg>
    <div class="ribbon__label">Breakfast</div>
  </div>
  <div class="ribbon" style="left:452px;top:503px">
    <svg width="300" height="85" viewBox="0 0 300 85" aria-hidden="true">
      <polygon points="0,34 54,34 54,78 0,78 18,56" fill="var(--pink-deep)"/>
      <polygon points="300,34 246,34 246,78 300,78 282,56" fill="var(--pink-deep)"/>
      <path d="M36,12 Q150,30 264,12 L264,62 Q150,80 36,62Z" fill="var(--pink)"/>
    </svg>
    <div class="ribbon__label">Something Light</div>
  </div>
  <div class="ribbon" style="left:860px;top:450px;transform:rotate(-2deg)">
    <svg width="320" height="85" viewBox="0 0 320 85" aria-hidden="true">
      <polygon points="0,34 56,34 56,78 0,78 18,56" fill="var(--mint-deep)"/>
      <polygon points="320,30 264,30 264,74 320,74 302,52" fill="var(--mint-deep)"/>
      <path d="M38,12 Q160,30 282,10 L282,60 Q160,80 38,62Z" fill="var(--mint)"/>
    </svg>
    <div class="ribbon__label">Hot Food and Sandwiches</div>
  </div>

  <!-- coffee -->
  <table class="coffee-table">
    <thead><tr><th class="drink"></th><th class="size-s">S</th><th class="size-l">L</th></tr></thead>
    <tbody>
      <tr><td class="drink">Latte</td><td class="size-s">$4.0</td><td class="size-l">$4.50</td></tr>
      <tr><td class="drink">Cappuccino</td><td class="size-s">$4.0</td><td class="size-l">$4.50</td></tr>
      <tr><td class="drink">Flat White</td><td class="size-s">$4.0</td><td class="size-l">$4.50</td></tr>
      <tr><td class="drink">Long Black</td><td class="size-s">$4.0</td><td class="size-l">$4.50</td></tr>
      <tr><td class="drink">Hot Chocolate</td><td class="size-s">$4.0</td><td class="size-l">$4.50</td></tr>
      <tr><td class="drink">Chai Latte</td><td class="size-s">$4.50</td><td class="size-l">$5.0</td></tr>
      <tr><td class="drink">Mocha</td><td class="size-s">$4.50</td><td class="size-l">$5.0</td></tr>
      <tr><td class="drink">Dirty Chai</td><td class="size-s">$5</td><td class="size-l">$5.50</td></tr>
    </tbody>
  </table>

  <ul class="short-list" style="list-style:none">
    <li>Espresso <span class="price">$3.50</span></li>
    <li>Short Macchiato <span class="price">$4.0</span></li>
    <li>Piccolo <span class="price">$4.0</span></li>
    <li>Long Macchiato <span class="price">$4.50</span></li>
  </ul>

  <div class="extras">
    <p class="extras__title">EXTRAS</p>
    <p>Soy Milk/Lactose Free Milk/Syrups/Extra Shot/Decaf&nbsp; <span class="price">$0.50</span> extra</p>
  </div>

  <ul class="food-list food-list--breakfast">
    <li>Bacon, Egg and Cheese Roll <span class="price">$6.0</span></li>
    <li>Ham and Cheese Toastie <span class="price">$5.0</span></li>
    <li>Cheese and Tomato Toastie <span class="price">$5.0</span></li>
    <li>Ham and Cheese Croissant <span class="price">$6.0</span></li>
    <li>Cheese and Tomato Croissant <span class="price">$5.50</span></li>
    <li>Plain Croissant <span class="price">$3.50</span></li>
    <li>Hash Brown <span class="price">$2.0</span></li>
    <li>2 Piece Toast <span class="price">$3.0</span></li>
    <li>2 Piece Rasin Toast <span class="price">$3.0</span></li>
  </ul>

  <ul class="food-list food-list--light">
    <li>Mixed Yoghurts <span class="price">$5.50</span></li>
    <li>Chia Pudding <span class="price">$5.50</span></li>
    <li>Fruit Salad <span class="price">$5.50</span></li>
    <li>Bircher Muesli <span class="price">$5.50</span></li>
    <li>Protein Balls <span class="price">$4.0</span></li>
    <li>Banana Bread <span class="price">$4.50</span></li>
    <li>Muffins <span class="price">$4.50</span></li>
    <li>Slices <span class="price">$4.0</span></li>
  </ul>

  <ul class="food-list food-list--hot">
    <li>Pre Made Sandwiches <span class="price">$6.50 - $7.50</span></li>
    <li>Pre Made Focaccias <span class="price">$8.50</span></li>
    <li>Wraps <span class="price">$7.50</span></li>
    <li>Vegetarian Salad <span class="price">$7.50</span></li>
    <li>Meat/Seafood Salad <span class="price">$9.50</span></li>
    <li>Hot Chips <span class="price">$4.50</span></li>
    <li>Dim Sim <span class="price">$1.50</span></li>
    <li>Potato Cake <span class="price">$1.50</span></li>
    <li>Plain Hamburger <span class="price">$7.50</span></li>
    <li>Hamburger with the lot <span class="price">$9.0</span></li>
    <li>Chicken Schnitzel Burger <span class="price">$8.50</span></li>
  </ul>

</main>
</body>
</html>
```